Stationery set created from logo

Existing logo design from successful designer T94. Thanks T94.

We now now need letterhead, business card design and background slide for powerpoint presentations. These need to be provided as PDF; JPEG and AI files.

I also need the names of the fonts used and the RGB colour/PMS colour names

Thankyou for submitting your designs. A design has been selcted. I appreciate youtr work. God wishes to you

```html
<!DOCTYPE html>
<html lang="en">
<head>
<meta charset="utf-8">
<title>Meridian Letterhead</title>
<link href="https://fonts.googleapis.com/css2?family=Arimo:wght@400;700&display=swap" rel="stylesheet">
<style>
  :root {
    --brand-blue: #3399e0;
    --heading-blue: #2f8fd8;
    --brand-purple: #3d2f7a;
    --ink: #3a3a3a;
    --muted: #6b6b6b;
    --paper: #ffffff;
    --frame: #222222;
  }
  html, body {
    margin: 0;
    padding: 0;
    width: 919px;
    height: 1200px;
    overflow: hidden;
    background: var(--paper);
  }
  .letterhead {
    position: relative;
    width: 919px;
    height: 1200px;
    font-family: "Arimo", Arial, sans-serif;
    color: var(--ink);
  }
  .page-art {
    position: absolute;
    inset: 0;
  }
  .company-address {
    position: absolute;
    left: 648px;
    top: 97px;
    margin: 0;
    color: var(--paper);
    font-style: normal;
    font-weight: 700;
    font-size: 13px;
    line-height: 18.5px;
  }
  .company-address .label { font-size: 14.5px; }
  .brand {
    position: absolute;
    left: 190px;
    top: 196px;
    display: flex;
    align-items: center;
    gap: 10px;
  }
  .brand-dot {
    width: 22px;
    height: 22px;
    border-radius: 50%;
    background: var(--brand-blue);
  }
  .brand-name {
    font-weight: 700;
    font-size: 34px;
    letter-spacing: 1.5px;
    color: var(--brand-purple);
  }
  .salutation {
    position: absolute;
    left: 255px;
    top: 424px;
    margin: 0;
    color: var(--heading-blue);
    font-weight: 700;
    font-size: 14px;
  }
  .letter-body {
    position: absolute;
    left: 255px;
    top: 482px;
    width: 482px;
    font-size: 10.1px;
    line-height: 17.8px;
  }
  .letter-body p { margin: 0 0 17px; }
  .sign-off {
    position: absolute;
    left: 626px;
    top: 897px;
    color: var(--muted);
    font-size: 11px;
  }
  .signature {
    position: absolute;
    left: 606px;
    top: 914px;
    width: 160px;
    height: 72px;
    background: linear-gradient(100deg, #f6f6f6, #e8e8e8 60%, #f6f6f6);
    border-radius: 36px;
  }
  .signer-name {
    position: absolute;
    left: 626px;
    top: 994px;
    color: var(--muted);
    font-size: 11.5px;
  }
  .signer-title {
    position: absolute;
    left: 626px;
    top: 1010px;
    color: var(--ink);
    font-size: 9.5px;
  }
</style>
</head>
<body>
<main class="letterhead">
  <svg class="page-art" width="919" height="1200" viewBox="0 0 919 1200" aria-hidden="true">
    <rect class="page-frame" x="43.5" y="43.5" width="830" height="1075" fill="none" stroke="var(--frame)" stroke-width="1"/>
    <rect class="blue-field" x="55" y="55" width="805" height="1050" fill="var(--brand-blue)"/>
    <path class="content-panel" fill="var(--paper)"
      d="M330,55 C620,90 860,420 860,760 L860,1105 L300,1105 C130,980 70,760 70,560 C70,300 170,90 330,55 Z"/>
  </svg>

  <address class="company-address">
    <span class="label">Company Address:</span><br>
    Street 4120<br>
    ZIP Code: 3308<br>
    Phone: 555- 210- 4410<br>
    Fax: 555- 210- 4411
  </address>

  <div class="brand">
    <span class="brand-dot"></span>
    <span class="brand-name">MERIDIAN</span>
  </div>

  <h1 class="salutation">Dear Mr. Dennis</h1>

  <section class="letter-body">
    <p>Lorem ipsum dolor sit amet, consectetur adipiscing elit. Vestibulum adipiscing felis ac tortor consectetur feugiat. Etiam malesuada sodales eros ut ornare. Sed lorem eros, mattis id pretium ut, faucibus sit amet quam. Nullam consectetur ultricies ipsum, fringilla porttitor erat ornare at. Sed sit amet dui vel sapien ultrices vulputate. In hac habitasse platea dictumst. Nam est nisi, rhoncus at sagittis a, porttitor adipiscing nulla. Vivamus placerat felis ultrices quam iaculis eget dignissim felis egestas. Integer nec molestie lorem. Sed odio tellus, vulputate sed laoreet non, vulputate id justo. Etiam suscipit, odio vel auctor dictum, felis turpis ullamcorper neque, quis sodales risus metus in magna. Morbi pellentesque justo et quam laoreet facilisis. Aenean placerat, urna ornare aliquet tincidunt, lorem justo molestie ligula, id placerat est metus nec lectus. Nullam eu ipsum quis turpis tristique iaculis rutrum nec nibh. Phasellus risus eros, semper sit amet faucibus sit amet, laoreet et neque. Donec eros sem, viverra dictum faucibus quis, ullamcorper tincidunt nulla.</p>
    <p>Aenean ut congue tellus. Class aptent taciti sociosqu ad litora torquent per conubia nostra, per inceptos himenaeos. Sed facilisis, velit tincidunt pharetra fermentum, urna tortor iaculis erat, vitae sollicitudin leo mauris quis mi. Cras malesuada sem ac ipsum sagittis ultrices. Mauris fermentum porttitor nisi, eu facilisis lorem consectetur et. Suspendisse est elit, scelerisque ac euismod id, scelerisque viverra odio. Nullam scelerisque metus in eros semper congue. Fusce a fermentum est. Ut ac leo dolor. Quisque dignissim mauris a neque luctus pretium ultrices risus sagittis. Aenean quam massa, rutrum ac hendrerit eu, interdum eu nulla. Curabitur a velit mauris, sed porta eros. Cras id egestas sapien. Proin non metus eget felis eleifend adipiscing. Nunc malesuada pharetra blandit.</p>
  </section>

  <div class="sign-off">Your sincerely:</div>
  <div class="signature" role="img" aria-label="Handwritten signature"></div>
  <div class="signer-name">Paul Dennis</div>
  <div class="signer-title">Office Manager</div>
</main>
</body>
</html>
```